Lumen 7 auto detail

Looking for a flyer for my auto detail business
Hand Wash
• Clay Bar Application
• Machine Buff Wax / Compound /
Polish Paint Correction
• Clean Interior & Exterior Glass
• Vacuum, Shampoo, & Steam Clean
Upholstery, Carpets, Seats, Mats, & Trunk
• Pet Hair Removal
• Clean headliner
• Clean Doors/ Trunk/Hood Jambs
• Air Blow & Clean all Cracks & Crevices • Clean & Shine Protect All Vinyl/
Dash/Door Panels/Middle Console
Cleaning/Conditioning of Leather
• Clean, Treat, Dress, & Polish Tires,
Rims, & Wheel Wells
• Bug & Tar Removal
• Dress Black Exterior Plastic
• Minor Scratch Removal
• Engine Compartment Detail
Headlight Restoration (if needed)
• Interior Fragrance
• DRY ICE BLASTING
At Lumen 7 Auto Detail, we pride ourselves on providing a unique and exceptional experience that sets us apart from other detailers. Here are a few key factors that make us stand out:
1. Attention to Detail: We live up to our name by going above and beyond in every aspect of our car detailing services. Our team of skilled technicians pays meticulous attention to every nook and cranny of your vehicle, ensuring that it receives the highest level of care and precision.
2. Customized Solutions: We understand that each car is unique, and so are our clients' needs. That's why we offer personalized solutions tailored to your specific requirements. Whether you need a basic wash and wax or a comprehensive paint correction, we will work with you to create a customized detailing plan that meets your expectations.
3. Cutting-Edge Technology: We stay at the forefront of the industry by utilizing the latest tools, products, and techniques. Our team is trained in the most advanced detailing methods, allowing us to achieve superior results and deliver a finish that exceeds your expectations.
4. Exceptional Customer Service: We believe in providing not only exceptional car detailing but also an exceptional customer experience. Our friendly and knowledgeable staff is always ready to assist you, answer your questions, and ensure that you have a positive and enjoyable experience at our facility.
5. Eco-Friendly Practices: We are committed to reducing our environmental impact by using eco-friendly cleaning products and techniques. Our detailing processes are designed to minimize water usage and waste generation, making us a responsible choice for those who care about the planet.
These factors, combined with our passion for cars and dedication to excellence, make Lumen 7 Auto Detail the premier choice for discerning car owners who seek a truly exceptional detailing experience.
We offer mobile services as well
Address 742 Corliss Ave. S., Renton, WA 98061

```html
<!DOCTYPE html>
<html lang="en">
<head>
<meta charset="utf-8">
<title>Lumen 7 Auto Detail – Flyer</title>
<link rel="stylesheet" href="https://fonts.googleapis.com/css2?family=Roboto+Condensed:wght@700;800&family=Rubik:wght@400;500;700&family=Montserrat:wght@400;500&display=swap">
<style>
  :root{
    --red:#e4191b;
    --red-dark:#a80d10;
    --black:#0b0b0c;
    --panel:#141416;
    --white:#ffffff;
    --silver-1:#f4f4f4;
    --silver-2:#b9b9bb;
    --line:#8d8d90;
    --stage:#d3d3d3;
  }
  *{box-sizing:border-box;margin:0;padding:0}
  html,body{width:1200px;height:2368px;overflow:hidden;background:var(--stage)}
  .flyer{
    position:absolute;left:60px;top:420px;width:1080px;height:1529px;overflow:hidden;
    background:radial-gradient(ellipse at 90% 70%,#2a2a2d 0%,var(--black) 55%),var(--black);
    color:var(--white);font-family:"Rubik",sans-serif;
  }
  .abs{position:absolute}

  /* brand */
  .brand{left:40px;top:46px;width:310px;display:flex;flex-direction:column;align-items:center;gap:14px;z-index:3}
  .brand-mark{width:150px;height:150px;border-radius:50%;background:#1c1c1e;border:6px solid var(--red);flex:none}
  .brand-name{font-family:"Roboto Condensed",sans-serif;font-weight:800;font-size:36px;line-height:1;color:var(--white);text-transform:uppercase;white-space:nowrap;text-align:center}

  /* photos */
  .hero-ring{left:370px;top:-125px;width:640px;height:640px;border-radius:50%;
    background:linear-gradient(160deg,var(--silver-1),#777 45%,var(--silver-1) 70%,#555);padding:12px}
  .hero-photo{width:100%;height:100%;border-radius:50%;border:5px solid var(--red);
    background:radial-gradient(circle at 70% 40%,#b8252a 0%,#5b1417 35%,#1b1b1d 70%)}
  .detail-ring{left:770px;top:182px;width:330px;height:330px;border-radius:50%;
    background:linear-gradient(200deg,var(--silver-1),#6d6d6f 50%,var(--silver-1));padding:10px}
  .detail-photo{width:100%;height:100%;border-radius:50%;border:5px solid var(--red);
    background:radial-gradient(circle at 45% 60%,#f7f7f7 0%,#e7b8b8 30%,#d6454a 65%,#a81c21)}

  /* frame lines */
  .frame{left:0;top:0;width:1080px;height:1529px;pointer-events:none}

  /* headline */
  .headline{left:58px;top:365px;font-family:"Roboto Condensed",sans-serif;font-weight:800;text-transform:uppercase;line-height:1}
  .headline .l1,.headline .l2{font-size:49px;display:block;margin-bottom:2px}
  .headline .big{font-size:74px;color:var(--red);display:block;margin:-2px 0 0}
  .headline .l4{font-size:35px;display:block;margin-top:2px}
  .headline .l5{font-size:30px}
  .headline .l5 em{font-style:normal;font-size:58px;color:var(--red)}
  .accent{color:var(--red)}

  /* reasons */
  .reasons{left:58px;top:644px;width:440px}
  .reason{height:124px}
  .reason-head{display:flex;align-items:stretch;height:30px;margin-bottom:10px}
  .reason-num{width:38px;background:var(--red-dark);font-family:"Roboto Condensed",sans-serif;font-weight:800;font-size:21px;display:flex;align-items:center;justify-content:center}
  .reason-title{background:var(--red);font-family:"Roboto Condensed",sans-serif;font-weight:800;font-size:21px;padding:0 24px 0 8px;display:flex;align-items:center;
    clip-path:polygon(0 0,100% 0,calc(100% - 10px) 100%,0 100%)}
  .reason-tick{width:4px;margin-left:8px;background:var(--red);transform:skewX(-14deg)}
  .reason p,.summary{font-family:"Montserrat",sans-serif;font-size:10.6px;line-height:1.28;color:#e9e9e9}
  .summary{left:58px;top:1246px;width:440px}

  /* services */
  .service{position:absolute;left:497px;width:560px;z-index:2}
  .service-icon{position:absolute;left:0;top:0;width:62px;height:62px;border-radius:50%;
    background:var(--white);border:4px solid var(--red);box-shadow:0 0 0 3px #aaa;display:flex;align-items:center;justify-content:center}
  .service-title{margin-left:62px;display:flex;flex-direction:column;gap:4px}
  .title-bar{display:inline-flex;align-items:center;align-self:flex-start;height:38px;padding:0 30px 0 16px;
    background:linear-gradient(180deg,var(--white),#c8c8ca);color:var(--red);
    font-family:"Rubik",sans-serif;font-weight:700;font-size:32px;white-space:nowrap;
    clip-path:polygon(0 0,calc(100% - 16px) 0,100% 50%,calc(100% - 16px) 100%,0 100%);position:relative}
  .title-wrap{display:flex;align-items:center;align-self:flex-start}
  .title-wrap::after{content:"";width:14px;height:38px;margin-left:2px;background:var(--red);
    clip-path:polygon(0 0,40% 0,100% 50%,40% 100%,0 100%,60% 50%)}
  .service ul{list-style:none;margin:12px 0 0 86px}
  .service li{font-family:"Rubik",sans-serif;font-size:17.5px;line-height:22.6px;color:var(--white);padding-left:20px;position:relative}
  .service li::before{content:"›";position:absolute;left:0;top:-1px;color:var(--red);font-weight:700}

  /* mobile banner */
  .mobile{left:0;top:1322px;width:484px;height:108px;z-index:2;
    background:linear-gradient(180deg,#fafafa,#bdbdbf 55%,#e5e5e5);
    clip-path:polygon(0 0,96% 0,100% 8%,100% 100%,0 100%);display:flex;align-items:center;padding-left:36px;gap:16px}
  .mobile-text{font-family:"Roboto Condensed",sans-serif;font-weight:800;font-size:37px;line-height:1;color:#111;text-transform:uppercase}
  .washer-art{left:6px;top:1438px;width:60px;height:60px;background:linear-gradient(135deg,#5d0a0c,#7a0f12);border-radius:8px;z-index:2}

  /* footer */
  .footer{left:0;top:1430px;width:1080px;height:99px;background:var(--red);display:flex;align-items:center;padding-left:80px}
  .contact{display:flex;align-items:center;gap:10px;color:var(--white)}
  .phone{font-family:"Roboto Condensed",sans-serif;font-weight:800;font-size:40px;margin-right:38px}
  .address{font-family:"Rubik",sans-serif;font-size:19px;line-height:1.2;margin-right:44px}
  .web{font-family:"Roboto Condensed",sans-serif;font-weight:800;font-size:34px}
</style>
</head>
<body>
<main class="flyer">

  <div class="abs hero-ring"><div class="hero-photo" role="img" aria-label="Detailer pressure-washing a foam-covered red sports car"></div></div>
  <div class="abs detail-ring"><div class="detail-photo" role="img" aria-label="Hand washing car paint with a soapy sponge"></div></div>

  <div class="abs brand">
    <div class="brand-mark"></div>
    <div class="brand-name">Lumen 7 Auto Detail</div>
  </div>

  <svg class="abs frame" viewBox="0 0 1080 1529" aria-hidden="true">
    <defs>
      <linearGradient id="steel" x1="0" x2="1"><stop offset="0" stop-color="#4a4a4d"/><stop offset=".5" stop-color="#9a9a9d"/><stop offset="1" stop-color="#4a4a4d"/></linearGradient>
      <radialGradient id="glow"><stop offset="0" stop-color="#ffffff" stop-opacity=".35"/><stop offset="1" stop-color="#ffffff" stop-opacity="0"/></radialGradient>
    </defs>
    <path d="M0 315 H420 L527 420 V1417 H1020 L1058 1380" fill="none" stroke="url(#steel)" stroke-width="4"/>
    <path d="M0 322 H414 L520 428" fill="none" stroke="#2b2b2e" stroke-width="5"/>
    <path d="M1080 1365 V1430 H940 Z" fill="var(--red)"/>
    <path d="M1080 1345 L1040 1385" stroke="#999" stroke-width="3"/>
    <circle cx="990" cy="1130" r="70" fill="url(#glow)"/>
  </svg>

  <h1 class="abs headline">
    <span class="l1">We are <span class="accent">unique</span></span>
    <span class="l2">and exceptional</span>
    <span class="big">Experience</span>
    <span class="l4">that sets us apart from</span>
    <span class="l5">other <em>detailers.</em></span>
  </h1>

  <section class="abs reasons">
    <div class="reason">
      <div class="reason-head"><span class="reason-num">1.</span><span class="reason-title">ATTENTION TO DETAIL:</span><span class="reason-tick"></span></div>
      <p>We live up to our name by going above and beyond in every aspect of our car detailing services. Our team of skilled technicians pays meticulous attention to every nook and cranny of your vehicle, ensuring that it receives the highest level of care and precision.</p>
    </div>
    <div class="reason">
      <div class="reason-head"><span class="reason-num">2.</span><span class="reason-title">CUSTOMIZED SOLUTIONS:</span><span class="reason-tick"></span></div>
      <p>We understand that each car is unique, and so are our clients' needs. That's why we offer personalized solutions tailored to your specific requirements. Whether you need a basic wash and wax or a comprehensive paint correction, we will work with you to create a customized detailing plan that meets your expectations.</p>
    </div>
    <div class="reason">
      <div class="reason-head"><span class="reason-num">3.</span><span class="reason-title">CUTTING-EDGE TECHNOLOGY:</span><span class="reason-tick"></span></div>
      <p>We stay at the forefront of the industry by utilizing the latest tools, products, and techniques. Our team is trained in the most advanced detailing methods, allowing us to achieve superior results and deliver a finish that exceeds your expectations.</p>
    </div>
    <div class="reason">
      <div class="reason-head"><span class="reason-num">4.</span><span class="reason-title">EXCEPTIONAL CUSTOMER SERVICE:</span><span class="reason-tick"></span></div>
      <p>We believe in providing not only exceptional car detailing but also an exceptional customer experience. Our friendly and knowledgeable staff is always ready to assist you, answer your questions, and ensure that you have a positive and enjoyable experience at our facility.</p>
    </div>
    <div class="reason">
      <div class="reason-head"><span class="reason-num">5.</span><span class="reason-title">ECO-FRIENDLY PRACTICES:</span><span class="reason-tick"></span></div>
      <p>We are committed to reducing our environmental impact by using eco-friendly cleaning products and techniques. Our detailing processes are designed to minimize water usage and waste generation, making us a responsible choice for those who care about the planet.</p>
    </div>
  </section>
  <p class="abs summary">These factors, combined with our passion for cars and dedication to excellence, make Lumen 7 Auto Detail the premier choice for discerning car owners who seek a truly exceptional detailing experience.</p>

  <div class="service" style="top:478px">
    <div class="service-icon"><svg width="34" height="34" viewBox="0 0 24 24" fill="none" stroke="var(--red)" stroke-width="1.8"><path d="M4 15l2-5h12l2 5v4H4z"/><circle cx="8" cy="17" r="1.3"/><circle cx="16" cy="17" r="1.3"/><path d="M8 6c0-2 2-2 2-4M13 6c0-2 2-2 2-4"/></svg></div>
    <div class="service-title"><div class="title-wrap"><span class="title-bar">Hand Wash</span></div></div>
    <ul><li>Clay Bar Application</li><li>Machine Buff Wax / Compound /</li></ul>
  </div>

  <div class="service" style="top:593px">
    <div class="service-icon"><svg width="34" height="34" viewBox="0 0 24 24" fill="none" stroke="var(--red)" stroke-width="1.8"><rect x="5" y="3" width="9" height="8" rx="1"/><path d="M9 11v9M6 20h6M14 6h4"/></svg></div>
    <div class="service-title"><div class="title-wrap"><span class="title-bar">Polish Paint Correction</span></div></div>
    <ul><li>Clean Interior &amp; Exterior Glass</li><li>Vacuum, Shampoo, &amp; Steam Clean</li></ul>
  </div>

  <div class="service" style="top:712px">
    <div class="service-icon"><svg width="34" height="34" viewBox="0 0 24 24" fill="none" stroke="var(--red)" stroke-width="1.8"><rect x="8" y="2" width="8" height="10" rx="3"/><path d="M6 12h12v5H6zM8 17v4M16 17v4"/></svg></div>
    <div class="service-title">
      <div class="title-wrap"><span class="title-bar">Upholstery, Carpets, Seats,</span></div>
      <div class="title-wrap"><span class="title-bar">Mats, &amp; Trunk</span></div>
    </div>
    <ul><li>Pet Hair Removal</li><li>Clean headliner</li><li>Clean Doors/ Trunk/Hood Jambs</li><li>Air Blow &amp; Clean all Cracks &amp; Crevices</li><li>Clean &amp; Shine Protect All Vinyl/Dash/Door Panels/<br>Middle Console</li></ul>
  </div>

  <div class="service" style="top:955px">
    <div class="service-icon"><svg width="34" height="34" viewBox="0 0 24 24" fill="none" stroke="var(--red)" stroke-width="1.8"><circle cx="12" cy="12" r="9"/><circle cx="9" cy="10" r="2.5"/><circle cx="15" cy="14" r="2"/><circle cx="14" cy="7" r="1"/></svg></div>
    <div class="service-title">
      <div class="title-wrap"><span class="title-bar">Cleaning/Conditioning</span></div>
      <div class="title-wrap"><span class="title-bar">of Leather</span></div>
    </div>
    <ul><li>Clean, Treat, Dress, &amp; Polish Tires,</li></ul>
  </div>

  <div class="service" style="top:1092px">
    <div class="service-icon"><svg width="34" height="34" viewBox="0 0 24 24" fill="var(--red)"><path d="M3 8h13l3-3 2 2-3 3v2H12l-2 9H7l2-9H3z"/></svg></div>
    <div class="service-title"><div class="title-wrap"><span class="title-bar">Rims, &amp; Wheel Wells</span></div></div>
    <ul><li>Bug &amp; Tar Removal</li><li>Dress Black Exterior Plastic</li><li>Minor Scratch Removal</li><li>Engine Compartment Detail</li></ul>
  </div>

  <div class="service" style="top:1276px">
    <div class="service-icon"><svg width="34" height="34" viewBox="0 0 24 24" fill="none" stroke="var(--red)" stroke-width="1.8"><path d="M3 15l2-5h14l2 5v4H3z"/><circle cx="7" cy="15" r="1.5"/><circle cx="17" cy="15" r="1.5"/></svg></div>
    <div class="service-title"><div class="title-wrap"><span class="title-bar">Headlight Restoration</span></div></div>
    <ul><li>Interior Fragrance</li><li>DRY ICE BLASTING</li></ul>
  </div>

  <div class="abs mobile">
    <svg width="56" height="62" viewBox="0 0 24 26" fill="none" stroke="#222" stroke-width="2"><rect x="3" y="2" width="11" height="20" rx="2"/><path d="M8 18h1M13 10l7-7M18 3l3 3"/></svg>
    <div class="mobile-text">We offer mobile<br>services as well</div>
  </div>

  <footer class="abs footer">
    <div class="contact phone">
      <svg width="26" height="26" viewBox="0 0 24 24" fill="#fff"><path d="M6.6 10.8a15 15 0 006.6 6.6l2.2-2.2c.3-.3.7-.4 1-.2 1.1.4 2.3.6 3.6.6.6 0 1 .4 1 1V20c0 .6-.4 1-1 1A17 17 0 013 4c0-.6.4-1 1-1h3.5c.6 0 1 .4 1 1 0 1.3.2 2.5.6 3.6.1.3 0 .7-.2 1z"/></svg>
      <span>145-555-0192</span>
    </div>
    <div class="contact address">
      <svg width="24" height="30" viewBox="0 0 24 30" fill="#fff"><path d="M12 0a10 10 0 00-10 10c0 8 10 20 10 20s10-12 10-20A10 10 0 0012 0zm0 14a4 4 0 110-8 4 4 0 010 8z"/></svg>
      <span>Address 742 Corliss Ave. S.,<br>Renton, WA 98061</span>
    </div>
    <div class="contact web">
      <svg width="28" height="28" viewBox="0 0 24 24" fill="none" stroke="#fff" stroke-width="2"><circle cx="12" cy="12" r="10"/><path d="M2 12h20M12 2c3 3 3 17 0 20M12 2c-3 3-3 17 0 20"/></svg>
      <span>www.lumen7detail.com</span>
    </div>
  </footer>

  <div class="abs washer-art" role="img" aria-label="Pressure washer spray gun graphic"></div>
</main>
</body>
</html>
```